BrightHarbor Web Design Project

BrightHarbor IT solutions, a IT mananaged services company is looking to redesign current website (brightharborsolutions.example).

The website should convey professionalism within the managed it services community. The layout should invite users to explore other areas of the site. Should contain tools and other current information that clients or potential clients would find useful. Product pages, special offers and informational pages should be easily editable by non-programmers. Tidewardnet.example is a good site to review as an example of the design components we like.

Target Market(s)

Professional services companies with 10-100 users

Industry/Entity Type

It Company

Requirements
Must have
• • Clickable icons and graphics are good
• SEO - Wordpress could be a great platform for us to work from as we already have internal experience with it and it’s easy to update. If not Wordpress, we would need something that is easy to SEO optimize
• An “our team” section with pictures
• Sell the message to potential clients why they need managed services
• Home page needs to convey our core services at a glance
• Home page needs to load quickly
• Screenshots of our monitoring and security reports
• Easy for us to update/edit certain areas
o New products
o Testimonials
Nice to have
• • Something like TN’s savings calculator - http://www.tidewardnet.example/it-savings-calculator/
• Webform to enter service ticket requests
• Motion of home page banner
• Maybe pull in RSS feeds from current tech news sources
• Rotating content on all pages to keep it fresh
• “Harbor-up” feature for monthly promos
Should not have
• • Should not be overly "techie" in feel.
• Not overly wordy (like current site)

```html
<!DOCTYPE html>
<html lang="en">
<head>
<meta charset="utf-8">
<title>BrightHarbor IT Solutions</title>
<link href="https://fonts.googleapis.com/css2?family=Questrial&family=Carlito:wght@400;700&family=Arimo:ital,wght@0,400;0,700;1,400&display=swap" rel="stylesheet">
<style>
:root{
  --green:#5f9a1c;
  --green-dark:#3f6f10;
  --green-bar:#6f9a2e;
  --green-light:#8cc43c;
  --blue-title:#2a8ac8;
  --text:#222;
  --grey:#777;
  --panel-border:#d8d8d8;
  --white:#fff;
}
*{margin:0;padding:0;box-sizing:border-box}
html,body{width:1000px;height:1200px;overflow:hidden;background:var(--white)}
body{position:relative;font-family:Arimo,Arial,sans-serif;color:var(--text)}
.abs{position:absolute}

.brand{left:48px;top:14px;width:130px;text-align:center}
.brand-mark{width:62px;height:62px;border-radius:50%;background:var(--green-light);margin:0 auto 8px}
.brand-name{font-family:Questrial,sans-serif;font-size:19px;color:var(--green);line-height:1.05}

.contact{right:37px;top:38px;text-align:right;font-family:Questrial,sans-serif;font-style:italic}
.contact .tollfree{font-size:19px;color:var(--green-dark);letter-spacing:1px;font-weight:700}
.contact .tollfree b{color:#111}
.contact .phone{font-size:19px;color:#555;letter-spacing:1px;margin-top:10px}

.search{left:768px;top:106px;width:166px;height:23px;border:1px solid #bbb;border-radius:3px;background:#fff}
.search svg{position:absolute;left:6px;top:4px}
.go{left:940px;top:104px;width:35px;height:23px;border-radius:3px;background:linear-gradient(#9fd24f,#5c9a1a);color:#fff;font-weight:700;font-size:13px;text-align:center;line-height:23px}

.nav{left:18px;top:140px;width:962px;height:37px;border:1px solid var(--green-dark);border-radius:4px;background:linear-gradient(#8cc63c,#4e8a12);display:flex;align-items:center;list-style:none}
.nav li{color:#fff;font-size:15px;position:absolute;transform:translateX(-50%)}
.nav li.current{left:1px;top:1px;transform:none;width:90px;height:33px;background:linear-gradient(#fff,#e2e2e2);color:#222;text-align:center;line-height:33px;border-radius:3px 0 0 3px}

.hero{left:17px;top:180px;width:964px;height:368px;background:linear-gradient(#3c8fcf 0%,#7cbbe8 45%,#d6ecf7 75%,#8fc24a 92%,#5f9a1c 100%)}
.hero-text{left:311px;top:424px;font-size:17px;line-height:29px;color:#111}
.hero-text big{font-size:24px}
.slider{left:825px;top:499px;width:145px;height:18px;border-radius:9px;background:rgba(60,60,60,.8);display:flex;gap:11px;align-items:center;padding-left:14px}
.slider i{width:10px;height:10px;border-radius:50%;background:var(--green-light)}
.slider i:first-child{background:#fff}

.welcome{left:24px;top:574px;font-family:Questrial,sans-serif;font-size:25px;color:var(--green);text-decoration:underline;text-underline-offset:5px;text-decoration-thickness:1px}
.lead{left:28px;top:637px;width:700px;font-family:Questrial,sans-serif;font-size:19px;line-height:22px;color:#111}
.body-copy{left:30px;top:691px;width:680px;font-size:11.5px;line-height:14.5px;color:var(--grey)}
.body-copy p+p{margin-top:15px}
.read-more{left:610px;top:806px;font-size:11px;font-style:italic;color:var(--green-dark)}

.panel{border:1px solid var(--panel-border);border-radius:6px;background:linear-gradient(#fff 40%,#e6e6e6)}
.support{left:742px;top:579px;width:229px;height:243px}
.support-art{left:24px;top:32px;width:178px;height:138px;border-radius:4px;background:linear-gradient(135deg,#c8ccd0,#8fc0e0 55%,#7bb548)}
.support-btn{left:14px;top:180px;width:203px;height:35px;border-radius:6px;border:1px solid #6bc23c;background:linear-gradient(#3c8ed6,#124f8c);color:#fff;font-family:Questrial,sans-serif;font-size:19px;text-align:center;line-height:33px}

.card{top:840px;width:229px;height:263px}
.card-icon{left:50%;top:6px;transform:translateX(-50%);width:66px;height:60px;border-radius:6px}
.card-title{left:0;right:0;top:74px;text-align:center;font-family:Carlito,sans-serif;font-size:16px;color:var(--blue-title)}
.card ul{position:absolute;left:20px;top:103px;list-style:none;font-size:12px;color:#555}
.card li{position:relative;padding-left:14px;height:24px}
.card li::before{content:"";position:absolute;left:0;top:3px;border-left:7px solid var(--green);border-top:4px solid transparent;border-bottom:4px solid transparent}
.team li{height:43px;color:var(--green);}
.team li span{display:block;color:#555;font-size:11px;margin-top:2px}
.card-copy{position:absolute;left:12px;top:102px;width:205px;font-size:12px;line-height:24px;color:#555}
.card-sign{position:absolute;left:10px;top:224px;font-size:12.5px;font-weight:700;color:var(--green)}

.footer-bar{left:24px;top:1121px;width:945px;height:29px;background:var(--green-bar)}
.calc{left:25px;top:1111px;width:40px;height:44px;border-radius:5px;background:linear-gradient(#d5d5d5,#9a9a9a);border:1px solid #777}
.calc-label{left:71px;top:1129px;font-size:12px;font-style:italic;color:#fff}
.footer-nav{left:295px;top:1130px;display:flex;font-size:11px;color:#fff;list-style:none}
.footer-nav li+li::before{content:"|";margin:0 15px}
.copyright{left:28px;top:1163px;font-size:11px;font-style:italic;color:#999}
.copyright b{color:var(--green-dark);font-weight:400}
.social{top:1155px;width:28px;height:28px;border-radius:50%;background:radial-gradient(circle at 40% 35%,#8cc43c,#3f7a10);border:1px solid #777}
</style>
</head>
<body>

<header>
  <div class="abs brand">
    <div class="brand-mark"></div>
    <div class="brand-name">BrightHarbor IT Solutions</div>
  </div>
  <div class="abs contact">
    <div class="tollfree">Toll Free: <b>(800) 555-0142</b></div>
    <div class="phone">Phone: (480) 555-0187</div>
  </div>
  <div class="abs search">
    <svg width="13" height="13" viewBox="0 0 13 13"><circle cx="5" cy="5" r="3.8" fill="none" stroke="#555" stroke-width="1.8"/><line x1="8" y1="8" x2="12" y2="12" stroke="#555" stroke-width="2"/></svg>
  </div>
  <div class="abs go">Go</div>
  <ul class="abs nav">
    <li class="current">Home</li>
    <li style="left:148px">Solutions</li>
    <li style="left:251px">About Us</li>
    <li style="left:378px">IT Consulting</li>
    <li style="left:499px">IT Programs</li>
    <li style="left:613px">IT Security</li>
    <li style="left:738px">Data Backup</li>
    <li style="left:861px">Contact</li>
  </ul>
</header>

<section class="abs hero" role="img" aria-label="Banner photo: dandelion seeds drifting across a blue sky over green grass"></section>
<div class="abs hero-text">Every company needs to <big>GROW</big> to survive.<br>We make sure your <big>TECHNOLOGY</big> is ready for that growth when you are</div>
<div class="abs slider"><i></i><i></i><i></i><i></i><i></i><i></i></div>

<main>
  <h1 class="abs welcome">Welcome to Our Website</h1>
  <h2 class="abs lead" style="font-weight:400">BrightHarbor can help your business harness the power of new technology, making your business fast and efficient.</h2>
  <div class="abs body-copy">
    <p>In the information age of today, one must stay abreast of current technology in order to thrive. New advancements are made daily in dispersing information and collaborative computing. High-speed networks aid in the exchange of electronic information between businesses, their customers, vendors, and peers. Businesses that are quick to act and effectively implement this technology will rise to the top.</p>
    <p>Our specific service offerings including information technology planning, consulting, project management/implementation, data backup and recovery, security management, 24/7/365 remote monitoring and help desk assistance.</p>
  </div>
  <a class="abs read-more">Read more...</a>

  <aside class="abs panel support">
    <div class="abs support-art" role="img" aria-label="Illustration of a desktop computer tower and monitor"></div>
    <div class="abs support-btn">Remote support</div>
  </aside>

  <section class="abs panel card team" style="left:30px">
    <div class="abs card-icon" role="img" aria-label="Icon of a team gathered around circular arrows" style="background:linear-gradient(135deg,#3a8fd0,#7ab648,#f08a24)"></div>
    <h3 class="abs card-title" style="font-weight:400">Our Team</h3>
    <ul>
      <li>Jordan Vale<span>Founder</span></li>
      <li>Jordan Vale<span>Founder</span></li>
      <li>Jordan Vale<span>Founder</span></li>
    </ul>
  </section>

  <section class="abs panel card" style="left:267px">
    <div class="abs card-icon" role="img" aria-label="Icon of a monitoring screen with an eye" style="background:linear-gradient(135deg,#6fa8d0,#2b3a48)"></div>
    <h3 class="abs card-title" style="font-weight:400">Monitoring &amp; Security Service</h3>
    <p class="card-copy">Processes for inbound mail and internal mail servers are checked, including the time it takes for the server to process incoming mail.</p>
  </section>

  <section class="abs panel card" style="left:503px">
    <div class="abs card-icon" role="img" aria-label="Icon of a computer monitor showing charts" style="background:linear-gradient(135deg,#9aa4ad,#1f3c5a)"></div>
    <h3 class="abs card-title" style="font-weight:400">New products</h3>
    <ul style="left:14px;top:104px">
      <li>Our Cloud Database Environment</li>
      <li>Business Intelligence</li>
      <li>ERP Advantage</li>
      <li>Clinic ERP Suite</li>
      <li>Mobile Solutions</li>
      <li>Our Cloud Database Environment</li>
    </ul>
  </section>

  <section class="abs panel card" style="left:742px">
    <div class="abs card-icon" role="img" aria-label="Icon of a person in a business suit" style="background:linear-gradient(#8a939c,#2c3440);width:54px"></div>
    <h3 class="abs card-title" style="font-weight:400">Testimonials</h3>
    <p class="card-copy">“BrightHarbor is a outstanding among IT consulting firms because they bring a wealth of knowledge and maturity, a demonstrated work ethic and strong leadership skills to their work …</p>
    <div class="card-sign">Jordan Vale, Northfield Labs</div>
  </section>
</main>

<footer>
  <div class="abs footer-bar"></div>
  <div class="abs calc" role="img" aria-label="Calculator icon"></div>
  <div class="abs calc-label">Calculate IT infrastructure</div>
  <ul class="abs footer-nav">
    <li>Home</li><li>Solutions</li><li>About Us</li><li>IT Consulting</li><li>IT Programs</li><li>IT Security</li><li>Data Backup</li><li>Contact</li>
  </ul>
  <div class="abs copyright">© 2012 All copyrights reserved by <b>BrightHarbor</b> IT Solutions</div>
  <div class="abs social" style="left:868px" aria-label="Social link"></div>
  <div class="abs social" style="left:904px" aria-label="Social link"></div>
  <div class="abs social" style="left:940px" aria-label="News feed link"></div>
</footer>

</body>
</html>
```